Sign for Pilates Studio

Cute and fun sandwich board sign ( 36" x 24" ) for outstanding Pilates studio in Santa Cruz. Sign should have logo, use the phrase "Pilates & Kinovane classes 7 Days a Week"
Updates

Dimensions are 36" x 24" and it should be clear and simple. The goal is to get people in the door. Try using the tree theme or the circle theme. Colors can be simple green, gold, burgundy....black lettering probably... Added Monday, January 12, 2015

Target Market(s)

Hip 30 year olds and everyone else too

Requirements
Must have
• It's a freestanding sign and should be simple to read
• Must say "Lark Hollow Pilates"
• "Pilates Classes 7 days A week"
Nice to have
• Logo, tree. green and gold colors
Should not have
• Not too busy. Easy to read while driving by

```html
<!DOCTYPE html>
<html lang="en">
<head>
<meta charset="utf-8">
<title>Lark Hollow Pilates – Sandwich Board Sign</title>
<link rel="stylesheet" href="https://fonts.googleapis.com/css2?family=Alegreya:wght@500&family=Maven+Pro:wght@500;600&display=swap">
<style>
  :root {
    --page-bg: #e9e6ea;
    --frame: #2b2b2d;
    --purple-dark: #7a3a8c;
    --purple: #934aa6;
    --purple-light: #a65cb8;
    --green: #8dc63f;
    --ink: #141014;
    --pose-dark: #2a1a2e;
  }
  * { box-sizing: border-box; margin: 0; padding: 0; }
  html, body {
    width: 1200px;
    height: 1000px;
    overflow: hidden;
    background: var(--page-bg);
  }
  .canvas {
    position: relative;
    width: 1200px;
    height: 1000px;
  }
  .sign {
    position: absolute;
    left: 300px;
    top: 50px;
    width: 600px;
    height: 900px;
    border: 12px solid var(--frame);
    background: linear-gradient(160deg, var(--purple-light) 0%, var(--purple) 45%, var(--purple-dark) 100%);
    text-align: center;
  }
  .brand {
    position: absolute;
    top: 120px;
    left: 0;
    right: 0;
    display: flex;
    align-items: center;
    justify-content: center;
    gap: 20px;
  }
  .brand-dot {
    flex: none;
    width: 120px;
    height: 120px;
    border-radius: 50%;
    background: var(--green);
  }
  .brand-text {
    text-align: left;
  }
  .brand-name {
    font-family: "Alegreya", serif;
    font-weight: 500;
    font-size: 56px;
    line-height: 0.95;
    color: var(--ink);
  }
  .brand-tagline {
    margin-top: 10px;
    font-family: "Maven Pro", sans-serif;
    font-weight: 500;
    font-size: 22px;
    color: var(--green);
  }
  .headline {
    position: absolute;
    top: 370px;
    left: 0;
    right: 0;
    font-family: "Alegreya", serif;
    font-weight: 500;
    font-size: 66px;
    line-height: 1;
    color: var(--ink);
  }
  .schedule {
    position: absolute;
    top: 442px;
    left: 0;
    right: 0;
    font-family: "Maven Pro", sans-serif;
    font-weight: 500;
    font-size: 62px;
    line-height: 1;
    color: var(--green);
  }
  .poses {
    position: absolute;
    top: 550px;
    left: 0;
    right: 0;
    display: flex;
    justify-content: center;
    gap: 18px;
  }
  .pose {
    width: 132px;
    height: 132px;
    border-radius: 50%;
    border: 9px solid var(--green);
    background: radial-gradient(circle, var(--pose-dark) 0%, #4a2a55 45%, var(--purple) 80%);
  }
  .phone-bar {
    position: absolute;
    top: 690px;
    left: 24px;
    width: 540px;
    height: 110px;
    border-radius: 10px;
    background: var(--green);
    display: flex;
    align-items: center;
    justify-content: center;
    font-family: "Maven Pro", sans-serif;
    font-weight: 500;
    font-size: 72px;
    color: var(--ink);
    letter-spacing: 1px;
  }
</style>
</head>
<body>
  <main class="canvas">
    <section class="sign">
      <div class="brand">
        <span class="brand-dot"></span>
        <div class="brand-text">
          <div class="brand-name">Lark Hollow<br>Pilates</div>
          <div class="brand-tagline">Pilates &amp; Kinovane Studio</div>
        </div>
      </div>

      <h1 class="headline">Pilates Classes</h1>
      <p class="schedule">7 days a week</p>

      <div class="poses">
        <div class="pose" role="img" aria-label="Silhouette of a person in a seated Pilates pose inside a green ring"></div>
        <div class="pose" role="img" aria-label="Silhouette of a person in a leg-raise Pilates pose inside a green ring"></div>
        <div class="pose" role="img" aria-label="Silhouette of a person in a side-plank Pilates pose inside a green ring"></div>
      </div>

      <div class="phone-bar">831 555 0142</div>
    </section>
  </main>
</body>
</html>
```